Concierge Dental / Medical Supply Ordering Business - Sleek, Efficient, Professional, Elite

www.brixtonfaymedical.example - example website.

We are a concierge supply ordering business for medical and dental that provide DSO price savings on supplies while maintaining business autonomy and independence.

We want a very simple website that looks very professional says what we do and gives a very simple method to contact us & sign up as above.

Target Market(s)

Independent Dental and Medical Practices

Industry/Entity Type

Dental and Medical - healthcare

Coding

Coded - Design and coding required

Number of Pages Required

3 page

Font styles to use
Sans Serif

Colors
0054AA
0677BA
7BADD7
CADEEF
E8F1F8

Requirements
Must have
• Simple contact page, sleek efficient design, uncomplicated.
Nice to have
• Sign up page vs just a contact page.
Should not have
• Lots of pages, hard to navigate,

```html
<!DOCTYPE html>
<html lang="en">
<head>
<meta charset="utf-8">
<title>Brixton Fay Supply</title>
<link href="https://fonts.googleapis.com/css2?family=Poppins:wght@600;700&family=Roboto:wght@400;500;700&display=swap" rel="stylesheet">
<style>
:root{
  --blue:#0aa2e3;
  --navy:#0054AA;
  --mid:#0677BA;
  --sky:#7BADD7;
  --pale:#CADEEF;
  --mist:#E8F1F8;
  --ink:#111;
  --text:#333;
  --muted:#8a8a8a;
  --dark:#1a1a1a;
}
*{box-sizing:border-box;margin:0;padding:0}
html,body{width:1200px;height:4370px;overflow:hidden}
body{font-family:"Roboto",Arial,sans-serif;color:var(--text);background:#fff;position:relative}
.abs{position:absolute}
h1,h2,h3{font-family:"Poppins",Arial,sans-serif;color:var(--ink);font-weight:700}
.accent{color:var(--blue)}
.btn{position:absolute;display:flex;align-items:center;justify-content:center;gap:8px;background:linear-gradient(#2f7fc0,#0f4f8c);color:#fff;font:500 14px "Roboto",sans-serif;text-transform:uppercase;border-radius:3px;box-shadow:0 3px 6px rgba(0,0,0,.2)}
.btn svg{width:14px;height:14px}
/* header */
.header{position:absolute;left:0;top:0;width:1200px;height:100px;background:#fff;z-index:3}
.brand-box{position:absolute;left:110px;top:0;width:192px;height:148px;background:#fff;z-index:4;display:flex;flex-direction:column;align-items:center;justify-content:center;gap:10px}
.brand-square{width:72px;height:72px;border-radius:14px;background:var(--pale)}
.brand-name{font:700 16px "Roboto",sans-serif;color:var(--ink)}
.nav{position:absolute;top:42px;left:436px;display:flex;font:400 15px "Roboto",sans-serif;color:#222}
.nav span{position:absolute;white-space:nowrap}
.search{position:absolute;left:1042px;top:30px;width:44px;height:44px;border-radius:50%;background:var(--blue);display:flex;align-items:center;justify-content:center}
/* hero */
.hero{position:absolute;left:0;top:100px;width:1200px;height:616px;background:linear-gradient(100deg,#dfeef8 0%,#b9d8ee 45%,#6fa7cf 75%,#cfe3f1 100%)}
.hero-card{position:absolute;left:93px;top:151px;width:494px;height:312px;border-radius:20px;background:rgba(255,255,255,.72)}
.hero-card h2{position:absolute;left:29px;top:40px;font-size:37px;color:var(--blue);font-weight:700}
.hero-card h1{position:absolute;left:29px;top:88px;font-size:43px;white-space:nowrap}
.hero-card p{position:absolute;left:29px;top:152px;width:440px;font-size:15.5px;line-height:26px;color:#222}
/* about */
.about-img{position:absolute;left:122px;top:803px;width:472px;height:398px;border-radius:42px;border:4px solid #777;background:linear-gradient(120deg,#e6edf2,#c9d6df 50%,#8b7c72)}
.about h2{position:absolute;left:657px;top:792px;font-size:40px}
.about p{position:absolute;left:657px;width:432px;font-size:15px;line-height:28px;text-align:justify;color:#444}
/* advocate */
.advocate{position:absolute;left:0;top:1286px;width:1200px;height:615px;background:#e3f2fb}
.advocate h2{position:absolute;left:0;width:1200px;top:60px;text-align:center;font-size:40px;line-height:44px}
.advocate p{position:absolute;left:154px;width:460px;font-size:15px;line-height:28px;text-align:justify;color:#444}
.deco{position:absolute;left:680px;top:205px;width:340px;height:340px;border-radius:60px;background:linear-gradient(135deg,#d8dde2,#6b6f74);display:flex;align-items:center;justify-content:center}
.deco span{font:700 30px "Roboto",sans-serif;color:#fff}
/* services */
.section-title{position:absolute;left:0;width:1200px;text-align:center;font-size:40px}
.svc{position:absolute;top:2126px;width:311px;height:252px;background:#fff;box-shadow:0 0 6px rgba(0,0,0,.15);text-align:center}
.svc-icon{position:absolute;left:95px;top:-59px;width:120px;height:120px;background:#fff;border:2px solid #9fd8f3;display:flex;align-items:center;justify-content:center}
.svc-icon div{width:110px;height:110px;background:var(--blue);display:flex;align-items:center;justify-content:center}
.svc h3{position:absolute;top:96px;width:100%;font:500 18px "Roboto",sans-serif;color:#111}
.svc p{position:absolute;top:128px;left:18px;right:18px;font-size:14px;line-height:26px;color:var(--muted)}
.more{position:absolute;font:500 14px "Roboto",sans-serif;color:var(--blue);display:flex;align-items:center;gap:6px}
.more svg{width:13px;height:13px}
.arrow{position:absolute;font:400 22px "Roboto",sans-serif;color:#333}
/* areas */
.areas{position:absolute;left:0;top:2469px;width:1200px;height:689px;background:linear-gradient(135deg,#0a8fd6,#1ea3e0 40%,#0c6fb8)}
.areas h2{color:#fff}
.area{position:absolute;width:475px;height:185px;background:#fff}
.area .ph{position:absolute;left:4px;top:4px;width:197px;height:177px}
.area h3{position:absolute;left:228px;top:30px;font:500 15px "Roboto",sans-serif;color:#111}
.area p{position:absolute;left:228px;top:58px;width:230px;font-size:13.5px;line-height:24px;color:var(--muted)}
/* testimonials */
.tcard{position:absolute;top:3355px;width:300px;height:265px;background:#fff;box-shadow:0 0 14px rgba(0,0,0,.12);text-align:center}
.avatar{position:absolute;left:110px;top:-45px;width:80px;height:80px;border-radius:50%;border:3px solid #e7eef3;background:linear-gradient(#d9c3a8,#8a6c55)}
.stars{position:absolute;top:60px;width:100%;color:#d4c21a;font-size:17px;letter-spacing:3px}
.tcard h3{position:absolute;top:87px;width:100%;font:500 16px "Roboto",sans-serif;color:#111}
.tcard p{position:absolute;top:116px;left:24px;right:24px;font-size:16px;line-height:26.5px;color:#333}
/* contact */
.touch{position:absolute;left:0;top:3704px;width:1200px;height:284px;background:linear-gradient(#2b64a0,#235a95)}
.touch h2{position:absolute;top:48px;width:1200px;text-align:center;color:#fff;font-size:40px}
.touch p{position:absolute;top:106px;width:1200px;text-align:center;color:#fff;font-size:15px;line-height:26px}
/* footer */
.footer{position:absolute;left:0;top:3988px;width:1200px;height:382px;background:var(--dark);color:#fff}
.footer h4{position:absolute;top:48px;font:500 16px "Roboto",sans-serif}
.footer ul{position:absolute;top:92px;list-style:none;font-size:13px;line-height:33px}
.f-brand{position:absolute;left:108px;top:62px;width:192px;display:flex;flex-direction:column;align-items:center;gap:12px}
.f-brand .brand-square{width:100px;height:100px;background:#4a4f55}
.f-brand .brand-name{color:#fff;font-size:19px}
.social{position:absolute;top:234px;left:135px;display:flex;gap:9px}
.social span{width:28px;height:28px;border:1.5px solid #fff;border-radius:50%}
.contact-item{position:absolute;left:879px;font-size:13px;line-height:18px;padding-left:24px}
.contact-item b{display:block;font-size:11.5px;font-weight:700}
.contact-item svg{position:absolute;left:0;top:2px;width:13px;height:13px}
.copy{position:absolute;top:334px;width:1200px;text-align:center;font-size:13px}
.top-btn{position:absolute;left:1105px;top:4275px;width:36px;height:36px;border-radius:50%;background:var(--blue);display:flex;align-items:center;justify-content:center}
</style>
</head>
<body>

<header class="header">
  <nav class="nav">
    <span style="left:0">HOME</span>
    <span style="left:80px">|</span>
    <span style="left:117px">ABOUT</span>
    <span style="left:202px">|</span>
    <span style="left:239px">SERVICE</span>
    <span style="left:333px">|</span>
    <span style="left:372px">FAQS</span>
    <span style="left:444px">|</span>
    <span style="left:482px">CONTACT US</span>
  </nav>
  <div class="search"><svg width="16" height="16" viewBox="0 0 16 16"><circle cx="7" cy="7" r="4.5" fill="none" stroke="#fff" stroke-width="2"/><line x1="10.3" y1="10.3" x2="14" y2="14" stroke="#fff" stroke-width="2.2" stroke-linecap="round"/></svg></div>
</header>
<div class="brand-box"><div class="brand-square"></div><div class="brand-name">Brixton Fay Supply</div></div>

<section class="hero" role="img" aria-label="Bright modern dental treatment room with a blue patient chair">
  <div class="hero-card">
    <h2>Welcome To</h2>
    <h1>Brixton Fay Supply</h1>
    <p>Lorem ipsum dolor sit amet, consectetur adipiscing elit sed do eiusmod tempor incididunt ut labore et dolore magna aliqua.</p>
    <a class="btn" style="left:29px;top:217px;width:161px;height:48px">Get Started <svg viewBox="0 0 14 14"><circle cx="7" cy="7" r="7" fill="#fff"/><path d="M5 4l4 3-4 3z" fill="#1f5f9c"/></svg></a>
  </div>
</section>

<section class="about">
  <div class="about-img" role="img" aria-label="Smiling doctor in a white coat talking with a patient across a desk"></div>
  <h2>About <span class="accent">Us</span></h2>
  <p style="top:849px">Lorem ipsum dolor sit amet, consectetur adipiscing elit, sed do eiusmod tempor incididunt ut labore et dolore magna aliqua. Ut enim ad minim veniam, quis nostrud exercitation ullamco laboris nisi ut aliquip ex ea commodo consequat. Duis aute irure dolor in reprehenderit in voluptate velit esse cillum dolore eu fugiat nulla pariatur. Excepteur sint occaecat .</p>
  <p style="top:1023px">Perspiciatis unde omnis iste natus error sit voluptatem accusantium doloremque laudantium, totam rem aperiam, eaque ipsa quae ab illo inventore veritatis et quasi architecto beatae vitae dicta sunt explicabo Nemo enim ipsam .</p>
  <a class="btn" style="left:657px;top:1152px;width:161px;height:48px">Learn More <svg viewBox="0 0 14 14"><circle cx="7" cy="7" r="7" fill="#fff"/><path d="M5 4l4 3-4 3z" fill="#1f5f9c"/></svg></a>
</section>

<section class="advocate">
  <h2>Advocating For Financial Transparency<br>In The <span class="accent">Medical Supply</span> World.</h2>
  <p style="top:195px">Lorem ipsum dolor sit amet, consectetur adipiscing elit, sed do eiusmod tempor incididunt ut labore et dolore magna aliqua. Ut enim ad minim veniam, quis nostrud exercitation ullamco laboris nisi ut aliquip ex ea commodo consequat. Duis aute irure dolor in reprehenderit in voluptate velit esse cillum dolore eu fugiat.</p>
  <p style="top:337px">Perspiciatis unde omnis isteds natused erorred sited voluptatem accusantium doloremque laudantium, totam rem aperiam, eaque ipsa quae ab illo inventore veritatis et quasi architecto beatae vitae dicta sunt explicabo Nemo enim ipsam .</p>
  <a class="btn" style="left:154px;top:469px;width:161px;height:48px">Learn More <svg viewBox="0 0 14 14"><circle cx="7" cy="7" r="7" fill="#fff"/><path d="M5 4l4 3-4 3z" fill="#1f5f9c"/></svg></a>
  <div class="deco"><span>Brixton Fay Supply</span></div>
</section>

<section class="services">
  <h2 class="section-title" style="top:1978px">Our <span class="accent">Services</span></h2>
  <span class="arrow" style="left:56px;top:2218px">‹</span>
  <span class="arrow" style="left:1131px;top:2218px">›</span>
  <div class="svc" style="left:110px">
    <div class="svc-icon"><div><svg width="64" height="64" viewBox="0 0 64 64" fill="none" stroke="#fff" stroke-width="2.5" stroke-linecap="round" stroke-linejoin="round"><path d="M14 14c6 4 8 14 8 22h24"/><path d="M22 36l4 10h22"/><path d="M36 46v8M28 56h16"/><path d="M38 10c8 0 14 6 14 14"/></svg></div></div>
    <h3>Lorem ipsum dolor sit amet</h3>
    <p>Lorem ipsum dolor consectetur adipiscing elit, sed do eiusmod tempor incididunt ut labore et dolore magna aliquad.</p>
    <span class="more" style="left:106px;top:214px">READ MORE <svg viewBox="0 0 14 14"><circle cx="7" cy="7" r="6" fill="none" stroke="#0aa2e3" stroke-width="1.6"/><path d="M5.5 4.5l3 2.5-3 2.5" fill="none" stroke="#0aa2e3" stroke-width="1.6"/></svg></span>
  </div>
  <div class="svc" style="left:441px">
    <div class="svc-icon"><div><svg width="64" height="64" viewBox="0 0 64 64" fill="none" stroke="#fff" stroke-width="2.5" stroke-linecap="round" stroke-linejoin="round"><path d="M20 28c0-6 6-8 12-5 6-3 12-1 12 5 0 6-3 8-4 14-1 5-2 12-5 12-2 0-2-8-3-8s-1 8-3 8c-3 0-4-7-5-12-1-6-4-8-4-14z"/><path d="M12 12l14 14M52 12L40 26"/></svg></div></div>
    <h3>Lorem ipsum dolor sit amet</h3>
    <p>Lorem ipsum dolor consectetur adipiscing elit, sed do eiusmod tempor incididunt ut labore et dolore magna aliquad.</p>
    <span class="more" style="left:106px;top:214px">READ MORE <svg viewBox="0 0 14 14"><circle cx="7" cy="7" r="6" fill="none" stroke="#0aa2e3" stroke-width="1.6"/><path d="M5.5 4.5l3 2.5-3 2.5" fill="none" stroke="#0aa2e3" stroke-width="1.6"/></svg></span>
  </div>
  <div class="svc" style="left:774px">
    <div class="svc-icon"><div><svg width="64" height="64" viewBox="0 0 64 64" fill="none" stroke="#fff" stroke-width="2.5" stroke-linecap="round" stroke-linejoin="round"><path d="M24 8c0-3 4-4 8-2 4-2 8-1 8 2 0 4-2 5-3 9s-2 8-5 8-4-4-5-8-3-5-3-9z"/><path d="M10 38c0-4 4-6 8-4 4-2 8 0 8 4 0 4-2 6-3 10-1 5-2 8-5 8s-4-3-5-8-3-6-3-10z"/><path d="M38 38c0-4 4-6 8-4 4-2 8 0 8 4 0 4-2 6-3 10-1 5-2 8-5 8s-4-3-5-8-3-6-3-10z"/></svg></div></div>
    <h3>Lorem ipsum dolor sit amet</h3>
    <p>Lorem ipsum dolor consectetur adipiscing elit, sed do eiusmod tempor incididunt ut labore et dolore magna aliquad.</p>
    <span class="more" style="left:106px;top:214px">READ MORE <svg viewBox="0 0 14 14"><circle cx="7" cy="7" r="6" fill="none" stroke="#0aa2e3" stroke-width="1.6"/><path d="M5.5 4.5l3 2.5-3 2.5" fill="none" stroke="#0aa2e3" stroke-width="1.6"/></svg></span>
  </div>
</section>

<section class="areas">
  <h2 class="section-title" style="top:52px">Areas of Practice</h2>
  <div class="area" style="left:110px;top:146px">
    <div class="ph" role="img" aria-label="Dentist treating a patient in a clinic chair" style="background:linear-gradient(135deg,#eef2f5,#b7c6d2)"></div>
    <h3>Lorem ipsum dolor sit amet</h3>
    <p>Lorem ipsum dolor sit aconsectetur tempor incididunt ut labore et dolore magna aliquat enim minim veniam.</p>
    <span class="more" style="left:228px;top:140px">READ MORE <svg viewBox="0 0 14 14"><circle cx="7" cy="7" r="6" fill="none" stroke="#0aa2e3" stroke-width="1.6"/><path d="M5.5 4.5l3 2.5-3 2.5" fill="none" stroke="#0aa2e3" stroke-width="1.6"/></svg></span>
  </div>
  <div class="area" style="left:614px;top:146px">
    <div class="ph" role="img" aria-label="Modern white dental surgery room" style="background:linear-gradient(135deg,#c9d4dd,#6e8598)"></div>
    <h3>Lorem ipsum dolor sit amet</h3>
    <p>Lorem ipsum dolor sit aconsectetur tempor incididunt ut labore et dolore magna aliquat enim minim veniam.</p>
    <span class="more" style="left:228px;top:140px">READ MORE <svg viewBox="0 0 14 14"><circle cx="7" cy="7" r="6" fill="none" stroke="#0aa2e3" stroke-width="1.6"/><path d="M5.5 4.5l3 2.5-3 2.5" fill="none" stroke="#0aa2e3" stroke-width="1.6"/></svg></span>
  </div>
  <div class="area" style="left:110px;top:351px">
    <div class="ph" role="img" aria-label="Gloved hands holding dental instruments" style="background:linear-gradient(135deg,#e9f1f7,#8fb7d6)"></div>
    <h3>Lorem ipsum dolor sit amet</h3>
    <p>Lorem ipsum dolor sit aconsectetur tempor incididunt ut labore et dolore magna aliquat enim minim veniam.</p>
    <span class="more" style="left:228px;top:140px">READ MORE <svg viewBox="0 0 14 14"><circle cx="7" cy="7" r="6" fill="none" stroke="#0aa2e3" stroke-width="1.6"/><path d="M5.5 4.5l3 2.5-3 2.5" fill="none" stroke="#0aa2e3" stroke-width="1.6"/></svg></span>
  </div>
  <div class="area" style="left:614px;top:351px">
    <div class="ph" role="img" aria-label="Surgical instruments laid out in an operating room" style="background:linear-gradient(135deg,#203a55,#3c6e97 60%,#c59a5a)"></div>
    <h3>Lorem ipsum dolor sit amet</h3>
    <p>Lorem ipsum dolor sit aconsectetur tempor incididunt ut labore et dolore magna aliquat enim minim veniam.</p>
    <span class="more" style="left:228px;top:140px">READ MORE <svg viewBox="0 0 14 14"><circle cx="7" cy="7" r="6" fill="none" stroke="#0aa2e3" stroke-width="1.6"/><path d="M5.5 4.5l3 2.5-3 2.5" fill="none" stroke="#0aa2e3" stroke-width="1.6"/></svg></span>
  </div>
  <a class="btn" style="left:519px;top:574px;width:161px;height:48px">View &nbsp;More <svg viewBox="0 0 14 14"><circle cx="7" cy="7" r="7" fill="#fff"/><path d="M5 4l4 3-4 3z" fill="#1f5f9c"/></svg></a>
</section>

<section class="testimonials">
  <h2 class="section-title" style="top:3238px">Our <span class="accent">Testimonials</span></h2>
  <span class="arrow" style="left:58px;top:3476px">‹</span>
  <span class="arrow" style="left:1127px;top:3476px">›</span>
  <div class="tcard" style="left:112px"><div class="avatar" role="img" aria-label="Client portrait"></div><div class="stars">★★★★★</div><h3>Jordan Hale</h3><p>Lorem ipsum dolo consectetur elit sed do eiusmod tempor incididunt ut labore et dolore magna aliqua. Uted enim ad minim veniam, quis nostrud exercitad magnad.</p></div>
  <div class="tcard" style="left:450px"><div class="avatar" role="img" aria-label="Client portrait"></div><div class="stars">★★★★★</div><h3>Jordan Hale</h3><p>Lorem ipsum dolo consectetur elit sed do eiusmod tempor incididunt ut labore et dolore magna aliqua. Uted enim ad minim veniam, quis nostrud exercitad magnad.</p></div>
  <div class="tcard" style="left:786px"><div class="avatar" role="img" aria-label="Client portrait"></div><div class="stars">★★★★★</div><h3>Jordan Hale</h3><p>Lorem ipsum dolo consectetur elit sed do eiusmod tempor incididunt ut labore et dolore magna aliqua. Uted enim ad minim veniam, quis nostrud exercitad magnad.</p></div>
</section>

<section class="touch">
  <h2>Get in Touch</h2>
  <p>For all questions, inquires regarding our services, or assistance in referring someone to us.<br>Please contact us below.</p>
  <a class="btn" style="left:519px;top:179px;width:161px;height:46px">Contact Us <svg viewBox="0 0 14 14"><circle cx="7" cy="7" r="7" fill="#fff"/><path d="M5 4l4 3-4 3z" fill="#1f5f9c"/></svg></a>
</section>

<footer class="footer">
  <div class="f-brand"><div class="brand-square"></div><div class="brand-name">Brixton Fay Supply</div></div>
  <div class="social"><span></span><span></span><span></span><span></span></div>
  <h4 style="left:423px">Quick Links</h4>
  <ul style="left:424px"><li>Home</li><li>About</li><li>Service</li><li>FAQs</li><li>Contact Us</li></ul>
  <h4 style="left:650px">About Company</h4>
  <ul style="left:650px"><li>Support</li><li>Terms &amp; Condition</li><li>Contact Us</li><li>Privacy Policy</li><li>FAQ</li></ul>
  <h4 style="left:879px">Contact Us</h4>
  <div class="contact-item" style="top:97px"><svg viewBox="0 0 14 14"><path d="M3 1l3 3-1.5 2c1 2 2 3 3.5 3.5L10 8l3 3-2 2C6 13 1 8 1 3z" fill="#0aa2e3"/></svg><b>Phone</b>+1 555 010 0199</div>
  <div class="contact-item" style="top:148px"><svg viewBox="0 0 14 14"><rect x="1" y="3" width="12" height="9" fill="#0aa2e3"/><path d="M1 3l6 5 6-5" fill="none" stroke="#1a1a1a" stroke-width="1.2"/></svg><b>Email</b>info@brixtonfaysupply.example</div>
  <div class="contact-item" style="top:199px"><svg viewBox="0 0 14 14"><path d="M7 1a4.5 4.5 0 0 1 4.5 4.5C11.5 9 7 13 7 13S2.5 9 2.5 5.5A4.5 4.5 0 0 1 7 1z" fill="#0aa2e3"/><circle cx="7" cy="5.5" r="1.6" fill="#1a1a1a"/></svg><b>Location</b>29 Lorem ipsum dolor sit amet<br>consectetur adipiscing elited</div>
  <div class="copy">2023 Copyright - Brixton Fay Supply. | All Rights Reserved</div>
</footer>
<div class="top-btn"><svg width="16" height="16" viewBox="0 0 16 16"><path d="M3 10l5-5 5 5" fill="none" stroke="#fff" stroke-width="2.2" stroke-linecap="round"/></svg></div>

</body>
</html>
```